Poster Design Project

I would like to include a picture of me meditating-
Include text: What are benefits of meditation-manage stress, reduce anxiety,improve relationships,create inner peace, awaken intuition, aid sleep patterns, lower blood pressure,become less judgemental, connect to spirit
2nd section- What is meditation: a tool to discover the bodies own inner intelligence.Its not about forcing the mind to be quiet, its about finding the stillness thats already there.
3rd section:
How will meditation improve my health? Doctors are increasingly citing stress as a major contributing factor to most illnesses.Research has shown meditation to be beneficial for wide range of health problems. As stress is greatly reduced through meditation- our minds and our bodies begin to function with maximum effectiveness.
I would like colours to be relaxing and soothing.

```html
<!DOCTYPE html>
<html lang="en">
<head>
<meta charset="utf-8">
<title>What are benefits of Meditation?</title>
<link href="https://fonts.googleapis.com/css2?family=Roboto+Condensed:wght@300;400;700&display=swap" rel="stylesheet">
<style>
  :root {
    --band: #5f6569;
    --paper: #ffffff;
    --ink: #55595c;
    --heading: #4a4f53;
    --mark: #111111;
    --photo-top: #ece6e0;
    --photo-bottom: #f6f5f3;
  }
  html, body {
    margin: 0;
    padding: 0;
    overflow: hidden;
    background: var(--paper);
  }
  .poster {
    position: relative;
    width: 960px;
    height: 1200px;
    overflow: hidden;
    background: var(--paper);
    font-family: "Roboto Condensed", "Arial Narrow", sans-serif;
    color: var(--ink);
  }
  .title-band {
    position: absolute;
    left: 0; top: 0;
    width: 960px; height: 125px;
    background: var(--band);
    display: flex;
    align-items: center;
    justify-content: center;
  }
  .title-band h1 {
    margin: 0;
    color: var(--paper);
    font-weight: 300;
    font-size: 42px;
    letter-spacing: 0.2px;
  }
  .meditation-photo {
    position: absolute;
    left: 265px; top: 255px;
    width: 455px; height: 655px;
    background: linear-gradient(180deg, var(--photo-top) 0%, var(--photo-bottom) 100%);
  }
  .benefit-arcs {
    position: absolute;
    left: 0; top: 0;
    width: 960px; height: 1000px;
  }
  .benefit-arcs text {
    font-family: "Roboto Condensed", "Arial Narrow", sans-serif;
    font-weight: 400;
    fill: var(--ink);
  }
  .studio-name {
    position: absolute;
    left: 380px; top: 808px;
    width: 260px;
    text-align: center;
    font-size: 38px;
    font-weight: 400;
    color: var(--mark);
    margin: 0;
  }
  .info {
    position: absolute;
    top: 975px;
  }
  .info h2 {
    margin: 0 0 10px;
    font-size: 26px;
    font-weight: 700;
    color: var(--heading);
  }
  .info p {
    margin: 0;
    font-size: 20px;
    line-height: 28px;
    font-weight: 400;
  }
  .info strong { font-weight: 700; color: var(--heading); }
  .info-what { left: 67px; width: 262px; }
  .info-health { left: 383px; width: 470px; }
  .footer-band {
    position: absolute;
    left: 0; bottom: 0;
    width: 960px; height: 18px;
    background: var(--band);
  }
</style>
</head>
<body>
<main class="poster">
  <header class="title-band">
    <h1>What are benefits of Meditation?</h1>
  </header>

  <div class="meditation-photo" role="img" aria-label="Photo of a woman in a white dress meditating cross-legged with eyes closed"></div>

  <svg class="benefit-arcs" viewBox="0 0 960 1000" aria-label="Benefits of meditation">
    <defs>
      <path id="outer-arc" d="M 229 691 A 320 320 0 1 1 732 689" fill="none"/>
      <path id="inner-arc" d="M 258 575 A 223 223 0 1 1 686 575" fill="none"/>
    </defs>
    <text font-size="31">
      <textPath href="#outer-arc" textLength="1425" lengthAdjust="spacingAndGlyphs">Manage Stress, Reduce Anxiety, Improve Relationships, Create Inner Peace, Awaken Intuition, Aid Sleep Patterns</textPath>
    </text>
    <text font-size="28">
      <textPath href="#inner-arc" textLength="800" lengthAdjust="spacingAndGlyphs">Lower Blood Pressure, Become Less Judgemental, Connect to Spirit</textPath>
    </text>
  </svg>

  <p class="studio-name">Sora Haven</p>

  <section class="info info-what">
    <h2>What is meditation?</h2>
    <p>A <strong>Tool</strong> to discover the bodies own <strong>Inner Intelligence</strong>. Its not about forcing the mind to be quiet, its about <strong>Finding the Stillness</strong> thats already there.</p>
  </section>

  <section class="info info-health">
    <h2>How will meditation improve my health?</h2>
    <p>Doctors are increasingly citing stress as a major contributing factor to most illnesses. Research has shown meditation to be beneficial for wide range of health problems. As stress is greatly reduced through meditation- our minds and our bodies begin to function with <strong>Maximum Effectiveness</strong>.</p>
  </section>

  <div class="footer-band"></div>
</main>
</body>
</html>
```